Tour Guide in Israel business card

I am a tour guide in Israel (the holy land). Prior to it I have over 20 years high-tech business. My main (but not only) focus is working with business people that come to Israel and want to get a tour (usually short from few hours to 2 days). During my guiding I incorporate a lot of my know how of the Israeli business culture. I like to have a business card that I can present to anyone that is looking for a tour guide, but that business people will understand the additional value I can provide them during my tour.

Target Market(s)

Business visitors and tourist to Israel

Industry/Entity Type

Tourism

Contact Information for Business Card

Dorian Kaplow
email: dorian@kaplowtours.net
Mobile: +972-52-7186450

Colors

Designer to choose colors to be used in the design.

Requirements
Must have
• Tour Guide
Nice to have
• I don't know how but it should project my understanding in business not just the tourist side of my knowledge.

```html
<!DOCTYPE html>
<html lang="en">
<head>
<meta charset="utf-8">
<title>Dorian Kaplow — Tour Guide Business Card</title>
<link rel="stylesheet" href="https://fonts.googleapis.com/css2?family=Oswald:wght@500&family=Work+Sans:wght@300;400&display=swap">
<style>
  :root {
    --backdrop: #1c1c1d;
    --card: #141414;
    --card-edge: #1f1f1f;
    --ink-gloss: #3a3a3a;
    --ink-gloss-hi: #4a4a4a;
    --ink-soft: #333333;
    --silver: #cfcfcf;
  }
  * { box-sizing: border-box; margin: 0; padding: 0; }
  html, body {
    width: 1200px;
    height: 900px;
    overflow: hidden;
    background: var(--backdrop);
  }
  .sheet {
    position: relative;
    width: 1200px;
    height: 900px;
    display: flex;
    flex-direction: column;
    align-items: center;
    justify-content: center;
    gap: 24px;
  }
  .card {
    position: relative;
    width: 700px;
    height: 400px;
    background: var(--card);
    border: 1px solid var(--card-edge);
    box-shadow: 0 18px 40px rgba(0, 0, 0, 0.55);
  }

  /* Front side */
  .card-front .title {
    position: absolute;
    right: 110px;
    top: 168px;
    font-family: "Work Sans", sans-serif;
    font-weight: 400;
    font-size: 42px;
    line-height: 1;
    letter-spacing: 5px;
    color: var(--silver);
    white-space: nowrap;
  }

  /* Back side */
  .card-back .identity {
    position: absolute;
    right: 448px;
    top: 170px;
    text-align: right;
  }
  .identity .name {
    font-family: "Oswald", sans-serif;
    font-weight: 500;
    font-size: 30px;
    line-height: 1;
    letter-spacing: 0.5px;
    color: var(--ink-gloss);
    text-shadow: 0 1px 0 var(--ink-gloss-hi);
    text-transform: uppercase;
    white-space: nowrap;
  }
  .identity .role {
    margin-top: 4px;
    font-family: "Work Sans", sans-serif;
    font-weight: 400;
    font-size: 13px;
    letter-spacing: 2.5px;
    color: var(--ink-gloss);
    text-transform: uppercase;
  }
  .card-back .divider {
    position: absolute;
    left: 274px;
    top: 168px;
    width: 1px;
    height: 54px;
    background: var(--ink-soft);
  }
  .card-back .contacts {
    position: absolute;
    left: 298px;
    top: 170px;
    list-style: none;
    font-family: "Work Sans", sans-serif;
    font-weight: 300;
    font-size: 21px;
    color: var(--ink-gloss);
    white-space: nowrap;
  }
  .contacts li {
    display: flex;
    align-items: center;
    gap: 14px;
    height: 27px;
  }
  .contacts svg {
    width: 13px;
    height: 13px;
    fill: none;
    stroke: var(--ink-gloss);
    stroke-width: 1.6;
  }
</style>
</head>
<body>
  <main class="sheet">
    <section class="card card-front" aria-label="Card front">
      <h1 class="title">TOUR GUIDE</h1>
    </section>

    <section class="card card-back" aria-label="Card back">
      <div class="identity">
        <p class="name">Dorian Kaplow</p>
        <p class="role">Director</p>
      </div>
      <div class="divider"></div>
      <ul class="contacts">
        <li>
          <svg viewBox="0 0 16 16" aria-hidden="true"><path d="M4 1.5 L6.5 5 L5 6.5 Q6.5 9.5 9.5 11 L11 9.5 L14.5 12 L13 14.5 Q6 14 1.5 3 Z"/></svg>
          <span>+972-52-7186450</span>
        </li>
        <li>
          <svg viewBox="0 0 16 16" aria-hidden="true"><rect x="1.5" y="3.5" width="13" height="9"/><path d="M1.5 3.5 L8 9 L14.5 3.5"/></svg>
          <span>dorian@kaplowtours.net</span>
        </li>
      </ul>
    </section>
  </main>
</body>
</html>
```